Web Design Project

Need a web design to be built by in-house team of developers. I need the look and feel of the site done ready for the developers to take over.

The site is a crowd funding site like www.pennyharbor.example. Our site will have all the main functions provided for on this site.
We are not looking for sophisticated investors, instead we are looking for people with an interest in investing but that need a lot of help and support through the process.

I have already obtained the logo. I attach it here.

I also want to have a coming soon page designed. I have sketched out what i want here and am uploading it in excel. this is obviously very basic and not what i will want for the main site.

colours should be light and accessible: blues, greens, yellows.

Site is to be fun and accessible.

site will have a lot of communication based aspects needed.

I am looking for a long term relationship with a designer to do this and to do many more things. I will have a lot of banners and desgin work to do here, and am looking ONLY for someone that can work on an ongoing basis (not full time, but a few hours a week).

I am also after an animation - basic 2 minute intro - not full animation, part powerpoint and part animation. I have made a separate tender for this, please quote me on it. I want the same person doing them all preferably....
Updates

Hi all

I am impressed with some of these designs. I have uploaded the wireframe of the coming soon page. 

I prefer the designs so far that are utilizing our little icons etc. 

obviously i understand you havent got root access or anything yet so are struggling to put them in, but its worth a try, some of the designs are using them well. 

i like bright colours. 

i would also show me how you are going to design other aspects eg chat box, forum page etc. 

Reason: i am going to choose a short list today and then deal only with those to get the final designs done.

Industry/Entity Type

Communication

Requirements
Must have
• the site will have all the functions of www.pennyharbor.example and www.backlantern.example.

```html
<!DOCTYPE html>
<html lang="en">
<head>
<meta charset="utf-8">
<title>Ideaspring – A new way to invest</title>
<link rel="stylesheet" href="https://fonts.googleapis.com/css2?family=Open+Sans:wght@400;600;700&family=Arimo:wght@400;700&family=Crimson+Text:wght@400;600&display=swap">
<style>
:root{
  --page-bg-top:#3f6f9f;
  --page-bg-mid:#6a9ccb;
  --panel:#ffffff;
  --nav-dark:#2b5178;
  --nav-light:#5d86b0;
  --nav-text:#eef3f8;
  --nav-active:#f7c531;
  --brand-blue:#1c6c9c;
  --heading-blue:#2f5c86;
  --text-grey:#5c5c5c;
  --body-text:#444;
  --link-blue:#24527e;
  --box-blue:#0d8ac6;
  --box-blue-dark:#0a6a9b;
  --orange:#f7a817;
  --orange-light:#ffd35a;
  --yellow-border:#f3c530;
  --progress-bg:#e3e3e3;
  --rule:#3a5c7e;
  --green-1:#c7e64a;
  --green-2:#6aa41f;
}
*{box-sizing:border-box;margin:0;padding:0}
html,body{width:1200px;height:900px;overflow:hidden}
body{
  font-family:"Open Sans",Verdana,sans-serif;
  background:linear-gradient(90deg,var(--page-bg-top) 0%,var(--page-bg-mid) 50%,var(--page-bg-top) 100%);
  position:relative;color:var(--body-text);
}
.page{position:absolute;left:81px;top:0;width:1022px;height:900px;background:var(--panel)}
.abs{position:absolute}
/* header */
.header{left:0;top:0;width:1022px;height:97px;background:linear-gradient(#fff 0%,#f2f2f2 55%,#d6d6d6 92%,#fff 100%)}
.brand{left:44px;top:34px;display:flex;align-items:center;gap:8px;font:700 24px "Arimo",sans-serif;color:var(--brand-blue)}
.brand-square{width:22px;height:22px;background:var(--box-blue)}
.account{left:672px;top:7px;font-size:13.5px;color:var(--link-blue)}
.account span{margin:0 8px}
.social-signin{left:800px;top:5px;width:180px;height:25px;border:1px solid #4a6ea8;background:#fff;display:flex;align-items:center;font-size:13.5px;color:var(--link-blue)}
.social-signin i{width:24px;height:23px;background:#3b5998;display:block;margin-right:6px}
/* nav */
.nav{left:0;top:97px;width:1022px;height:41px;background:linear-gradient(var(--nav-light),var(--nav-dark));display:flex;justify-content:flex-end;align-items:center;padding-right:42px;gap:32px}
.nav a{color:var(--nav-text);font-size:13px;text-decoration:none}
.nav a.active{color:var(--nav-active)}
/* intro */
.intro{left:0;top:138px;width:1022px;height:90px;background:linear-gradient(#dcdcdc,#fff 70%)}
.intro-title{left:42px;top:156px;font:700 21px "Arimo",sans-serif;color:var(--brand-blue)}
.intro-sub{left:42px;top:191px;font:700 18px "Arimo",sans-serif;color:var(--text-grey)}
.learn-more{left:836px;top:191px;font:700 18px "Arimo",sans-serif;color:var(--brand-blue);display:flex;align-items:center;gap:6px}
/* featured in */
.featured-in{left:20px;top:227px;width:982px;height:49px;border:1px solid #9a9a9a;border-radius:4px;display:flex;align-items:center;padding-left:45px;gap:18px}
.featured-in .label{font-size:13px;color:#888;letter-spacing:.5px;padding-right:18px;border-right:1px solid #bbb;margin-right:2px}
.press{height:26px;background:#efefef;padding:0 6px;display:flex;align-items:center;font:600 14px "Crimson Text",serif;color:#777;white-space:nowrap}
/* cta cards */
.cta{left:20px;width:288px;height:102px;border-radius:3px;overflow:hidden}
.cta-invest{top:285px;border:1px solid #888;background:linear-gradient(135deg,#d59a73,#8a6352 60%,#c9b9a5)}
.cta-raise{top:395px;border:2px solid var(--yellow-border);background:linear-gradient(135deg,#f3f0ec,#e7c9b6 55%,#f6f3ef)}
.cta-label{left:12px;top:5px;width:262px;height:24px;background:rgba(255,255,255,.8);font:700 13.5px "Open Sans",sans-serif;color:#444;padding:2px 7px}
.btn-blue{left:14px;top:64px;height:26px;padding:0 10px;border-radius:3px;background:linear-gradient(#1793cf,#0a679a);color:#fff;font-size:13px;line-height:26px}
.btn-yellow{left:13px;top:64px;height:26px;padding:0 9px;border-radius:3px;background:linear-gradient(var(--orange-light),#f2b92c);color:#333;font-size:13px;line-height:26px}
/* banner */
.banner{left:319px;top:285px;width:684px;height:211px;border:1px solid #999;border-radius:3px;overflow:hidden;background:linear-gradient(100deg,#9ccb3b 0%,var(--green-1) 45%,var(--green-2) 75%,#b9dd3c 100%)}
.banner-art{left:260px;top:0;width:424px;height:211px;background:linear-gradient(90deg,rgba(255,250,200,.45),rgba(255,255,255,.15) 40%,rgba(60,45,35,.3) 70%,rgba(0,0,0,0))}
.banner-card{left:2px;top:22px;width:380px;height:162px;background:rgba(255,255,255,.55)}
.banner-title{left:22px;top:35px;font:400 22px "Crimson Text",serif;color:#111}
.banner-text{left:23px;top:74px;width:345px;font:400 12.5px/14.5px "Arimo",sans-serif;letter-spacing:.55px;color:#111}
.banner-sign{left:23px;top:142px;font:600 15px/15px "Crimson Text",serif;color:#111}
.banner-more{left:176px;top:159px;font-size:12.5px;color:#111;font-family:"Arimo",sans-serif}
/* social counts */
.social-bar{left:21px;top:522px;width:286px;height:32px;border:1px solid #c9d3e2;border-radius:3px;display:flex;align-items:center;font-size:11px}
.social-bar .half{flex:1;display:flex;align-items:center;padding-left:25px;gap:4px}
.social-bar .half+.half{border-left:1px solid #c9d3e2;padding-left:24px}
.pill{border:1px solid #b8c6dc;border-radius:2px;background:#eef2f8;padding:1px 5px;color:#3b5a8a;font-weight:600}
.count{border:1px solid #c9d3e2;padding:1px 4px;color:#333}
/* video box */
.video{left:19px;top:565px;width:289px;height:183px;border-radius:4px;background:linear-gradient(var(--box-blue),var(--box-blue-dark));}
.video-title{left:19px;top:4px;font-size:11.5px;color:#fff}
.video-screen{left:5px;top:21px;width:278px;height:102px;background:#fff}
.video-name{left:0;top:14px;width:278px;text-align:center;font:700 20px "Arimo",sans-serif;color:var(--brand-blue)}
.video-caption{left:0;top:78px;width:278px;text-align:center;font-size:17px;color:#169ad6}
.video-play{left:104px;top:40px;width:60px;height:36px;background:rgba(60,90,110,.55);border-radius:6px}
.video-brand{left:212px;top:131px;font:700 16px "Arimo",sans-serif;color:#fff}
.video-controls{left:7px;top:161px;width:275px;height:12px;background:#e4e8ec;border-radius:2px;font-size:7px;color:#333;padding-left:40px;line-height:12px}
/* newsletter */
.newsletter{left:19px;top:758px;width:289px;height:73px;border-radius:4px;background:linear-gradient(var(--box-blue),var(--box-blue-dark))}
.newsletter h3{position:absolute;left:11px;top:5px;font:400 18px "Open Sans",sans-serif;color:#fff}
.news-input{left:11px;top:36px;width:181px;height:26px;background:#d4d4d4;border-radius:3px}
.news-btn{left:200px;top:36px;width:80px;height:26px;border-radius:3px;background:linear-gradient(var(--orange-light),var(--orange));font-size:13px;color:#333;text-align:center;line-height:26px}
/* blog */
.blog-box{left:19px;top:841px;width:289px;height:80px;border-radius:4px;background:linear-gradient(var(--box-blue),#1ea3dd)}
.blog-box h3{position:absolute;left:17px;top:8px;font:700 18px "Open Sans",sans-serif;color:#fff}
.blog-tab{left:17px;top:52px;width:93px;height:20px;background:#f6c26a}
/* pitches */
.pitches-title{left:327px;top:519px;font:700 23px "Open Sans",sans-serif;color:var(--heading-blue)}
.view-more{left:896px;top:524px;width:93px;height:24px;border-radius:2px;background:linear-gradient(var(--orange-light),var(--orange));font:700 13px "Open Sans",sans-serif;color:#333;text-align:center;line-height:24px}
.pitches-rule{left:319px;top:553px;width:683px;height:3px;background:var(--rule)}
.pitch{width:303px}
.pitch-name{font:400 17px "Open Sans",sans-serif;color:var(--heading-blue);position:absolute;left:0;top:0}
.pitch-photo{left:0;top:32px;width:130px;height:130px;background:linear-gradient(135deg,#cfd6de,#8fa4bd 50%,#d7dde3);border:1px solid #999}
.pitch-text{left:143px;top:33px;width:165px;font:400 12.5px/14.5px "Open Sans",sans-serif;letter-spacing:.45px;color:#555}
.pitch-foot{left:3px;top:168px;font:400 12.5px "Open Sans",sans-serif;letter-spacing:.3px;color:#555}
.progress{left:0;top:200px;width:302px;height:59px;border-radius:4px;background:var(--progress-bg)}
.bar{left:10px;top:10px;width:278px;height:22px;background:linear-gradient(#0f8fd0 0%,#0f8fd0 60%,#0a5f94 60%);border:1px solid #fff}
.bar-fill{left:0;top:0;width:19px;height:20px;background:linear-gradient(var(--orange) 50%,#ffd26a 50%);border-right:2px solid #fff}
.progress-text{left:10px;top:35px;font:400 15px "Open Sans",sans-serif;color:#222}
.progress-text b{color:var(--orange);font-weight:400}
.pitch-rule{left:0;top:281px;width:303px;height:1px;background:var(--rule)}
.pitch-next{left:0;top:300px}
</style>
</head>
<body>
<div class="page">
  <header class="header abs">
    <div class="brand abs"><span class="brand-square"></span>Ideaspring!</div>
    <div class="account abs">Log in<span>|</span>Sign up</div>
    <div class="social-signin abs"><i></i>Sign in with Linkbook</div>
  </header>
  <nav class="nav abs">
    <a class="active" href="#">Invest</a><a href="#">Get investment</a><a href="#">How it works</a><a href="#">About us</a><a href="#">Blog</a><a href="#">Forum</a>
  </nav>

  <section class="intro abs"></section>
  <h1 class="intro-title abs">A new way to invest...</h1>
  <p class="intro-sub abs">The world's first equity-based crowdfunding community dedicated to business investment</p>
  <div class="learn-more abs">
    <svg width="22" height="14" viewBox="0 0 22 14"><path d="M0 4h12V0l10 7-10 7v-4H0z" fill="#1c6c9c"/></svg>Learn more
  </div>

  <div class="featured-in abs">
    <span class="label">FEATURED IN</span>
    <span class="press">The Meridian</span>
    <span class="press">The Daily Courier</span>
    <span class="press">the sentinel</span>
    <span class="press">NBS</span>
    <span class="press">Brightwater</span>
    <span class="press">Market Times</span>
    <span class="press">The Herald</span>
  </div>

  <div class="cta cta-invest abs" role="img" aria-label="Photo of coins">
    <div class="cta-label abs">Invest in a business</div>
    <div class="btn-blue abs">Search pitches now</div>
  </div>
  <div class="cta cta-raise abs" role="img" aria-label="Photo of a hand signing a document">
    <div class="cta-label abs">Get Investment for your business</div>
    <div class="btn-yellow abs">Get investment now</div>
  </div>

  <div class="banner abs">
    <div class="banner-art abs" role="img" aria-label="Photo of a businesswoman drawing a chart on a green background"></div>
    <div class="banner-card abs"></div>
    <div class="banner-title abs">Blog Title text will go here.</div>
    <p class="banner-text abs">Text will go here. Text will go here. Text will go here. Text will go here. Text will go here. Text will go here. Text will go here. Text will go here. Text will go here. Text will go here.&nbsp; will go here.</p>
    <div class="banner-sign abs">Loram<br>Ipsum</div>
    <div class="banner-more abs">Click for more information</div>
  </div>

  <div class="social-bar abs">
    <div class="half"><span class="pill">Like</span><span class="count">302</span></div>
    <div class="half"><span class="pill">Chirp</span><span class="count">257</span></div>
  </div>

  <div class="video abs">
    <div class="video-title abs">Ideaspring! - How it works</div>
    <div class="video-screen abs">
      <div class="video-name abs">Ideaspring!</div>
      <div class="video-play abs"></div>
      <svg class="abs" style="left:126px;top:48px" width="16" height="20"><path d="M0 0l16 10L0 20z" fill="#fff"/></svg>
      <div class="video-caption abs">How it Works</div>
    </div>
    <div class="video-brand abs">ClipCast</div>
    <div class="video-controls abs">0:00 / 1:05</div>
  </div>

  <div class="newsletter abs">
    <h3>Newsletter</h3>
    <div class="news-input abs"></div>
    <div class="news-btn abs">Subscribe</div>
  </div>

  <div class="blog-box abs">
    <h3>Latest from our Blog</h3>
    <div class="blog-tab abs"></div>
  </div>

  <h2 class="pitches-title abs">Featured pitches</h2>
  <div class="view-more abs">view more</div>
  <div class="pitches-rule abs"></div>

  <article class="pitch abs" style="left:327px;top:569px">
    <h3 class="pitch-name">Real World Gallery</h3>
    <div class="pitch-photo abs" role="img" aria-label="Collage of business people around a globe"></div>
    <p class="pitch-text abs">Text will go here. Text will go here. Text will go here. Text will go here. Text will go here. Text will go here. Text will go here. Text will go here. Text will go here.&nbsp; will go here.</p>
    <p class="pitch-foot abs">Text will go here. Text will</p>
    <div class="progress abs"><div class="bar abs"><div class="bar-fill abs"></div></div><div class="progress-text abs"><b>10%</b> invested so far</div></div>
    <div class="pitch-rule abs"></div>
    <h3 class="pitch-name pitch-next">Real World Gallery</h3>
  </article>

  <article class="pitch abs" style="left:677px;top:569px">
    <h3 class="pitch-name">Real World Gallery</h3>
    <div class="pitch-photo abs" role="img" aria-label="Collage of business people around a globe"></div>
    <p class="pitch-text abs">Text will go here. Text will go here. Text will go here. Text will go here. Text will go here. Text will go here. Text will go here. Text will go here. Text will go here.&nbsp; will go here.</p>
    <p class="pitch-foot abs">Text will go here. Text will</p>
    <div class="progress abs"><div class="bar abs"><div class="bar-fill abs"></div></div><div class="progress-text abs"><b>10%</b> invested so far</div></div>
    <div class="pitch-rule abs"></div>
    <h3 class="pitch-name pitch-next">Real World Gallery</h3>
  </article>
</div>
</body>
</html>
```